Candle company needs a label for candle

Looking for a designer to create my candle label. I am going to attach a few pictures of my vision for the label as well as my Company Logo and jar I have puchased. I'm going for the modern rustic feel but you are the designer and have full trust in your abilities. The label is going to be printed on Kraft paper (2x3) so looking for the font to be black. The candle label MUST include the following information:
Candle Birchway Co.
NO. 01: Eucalyptus + Spearmint
Handmade In NJ
Soy Wax
9oz

Industry/Entity Type

Candle Industry

Colors

Designer to choose colors to be used in the design.

Requirements
Should not have
• Any images

```html
<!DOCTYPE html>
<html lang="en">
<head>
<meta charset="utf-8">
<title>Candle Birchway Co. — No.1 Eucalyptus &amp; Spearmint Label</title>
<link rel="stylesheet" href="https://fonts.googleapis.com/css2?family=Bodoni+Moda:wght@400&family=Jost:wght@400;500;600&family=Poiret+One&display=swap">
<style>
  :root {
    --ink: #000000;
    --charcoal: #38393b;
    --paper: #ffffff;
  }
  html, body {
    margin: 0;
    padding: 0;
    width: 1200px;
    height: 801px;
    overflow: hidden;
    background: var(--paper);
  }
  .label {
    display: block;
    width: 1200px;
    height: 801px;
  }
  .brand-name {
    font-family: "Jost", sans-serif;
    font-weight: 400;
    fill: var(--charcoal);
  }
  .series-number {
    font-family: "Bodoni Moda", serif;
    font-weight: 400;
    fill: var(--charcoal);
  }
  .scent-name {
    font-family: "Jost", sans-serif;
    font-weight: 500;
    fill: var(--ink);
  }
  .ampersand {
    font-family: "Bodoni Moda", serif;
    fill: var(--charcoal);
  }
  .origin {
    font-family: "Jost", sans-serif;
    font-weight: 600;
    fill: var(--charcoal);
  }
  .spec {
    font-family: "Poiret One", sans-serif;
    fill: var(--charcoal);
  }
  .rule {
    stroke: var(--charcoal);
    stroke-width: 5;
    fill: none;
  }
</style>
</head>
<body>
<svg class="label" viewBox="0 0 1200 801" xmlns="http://www.w3.org/2000/svg">
  <!-- brand -->
  <text class="brand-name" x="104" y="142" font-size="31">Candle Birchway Co.</text>

  <!-- series number -->
  <text class="series-number" x="494" y="231" font-size="260" textLength="528" lengthAdjust="spacingAndGlyphs">NO.1</text>

  <!-- scent -->
  <text class="scent-name" x="133" y="409" font-size="144" textLength="941" lengthAdjust="spacingAndGlyphs">EUCALYPTUS</text>
  <text class="ampersand" x="96" y="546" font-size="136">&amp;</text>
  <text class="scent-name" x="229" y="546" font-size="143" textLength="845" lengthAdjust="spacingAndGlyphs">SPEARMINT</text>

  <!-- details panel -->
  <g class="details">
    <polyline class="rule" points="424,620 103,620 103,801"/>
    <polyline class="rule" points="778,620 1074,620 1074,801"/>
    <line class="rule" x1="590" y1="656" x2="590" y2="801"/>
    <text class="origin" x="601" y="632" font-size="34" text-anchor="middle" letter-spacing="1">Handmade In NJ</text>
    <text class="spec" x="348" y="723" font-size="66" text-anchor="middle">Soy Wax</text>
    <text class="spec" x="836" y="723" font-size="66" text-anchor="middle">9 oz</text>
  </g>
</svg>
</body>
</html>
```